Varneck Law Business cards and stationary design project

We are looking for a stationary design for business cards (double sided), 8x10, 5x7, and legal and standard envelopes.

We would like the design to match the logo that we have already.
Color palate preferred is Teal, White, grey and any others that will look good for a professional law firm.

We would like this statement: "RELATIONSHIPS. RESPECT. RESULT" to be on the back of the business cards and maybe on the stationary if it looks good.

Please see link to website for more information: www.varneck-law-example.com

Target Market(s)

Potential clients that need Attorney services.

Industry/Entity Type

Law Firm

Contact Information for Business Card

We would like the front and back to be two different colors. Current business cards are teal front, grey back and are a vertical design. We are open to options with colors.

Font styles to use
Serif

Colors
33a6d7
33b8a4
b9b9b9
5c5c5c

Requirements
Must have
• Logo supplied needs to go on the card and stationary.
• Match website color palate, www.varneck-law-example.com
• Be professional and not too wordy.
• Criminal Law, Civil Litigation, Personal Injury, Restraining Orders need to be on the card.
Nice to have
• RELATIONSHIPS. RESPECT. RESULTS. on the back of the card.
Should not have
• Not be too busy/wordy or too flashy.

```html
<!DOCTYPE html>
<html lang="en">
<head>
<meta charset="utf-8">
<title>Varneck Law Stationery</title>
<link href="https://fonts.googleapis.com/css2?family=Jost:wght@400;500;600&display=swap" rel="stylesheet">
<style>
  :root {
    --teal: #2ab5a3;
    --grey-dark: #5c5c5c;
    --grey-light: #b9b9b9;
    --paper: #ffffff;
    --ink: #3a3a3a;
    --backdrop: #ecebe8;
  }
  * { box-sizing: border-box; margin: 0; padding: 0; }
  html, body { width: 1200px; height: 1200px; overflow: hidden; }
  body {
    background: var(--backdrop);
    font-family: "Jost", "Futura", sans-serif;
    color: var(--ink);
    position: relative;
  }
  .sheet {
    position: absolute;
    background: var(--paper);
    box-shadow: 0 2px 10px rgba(0,0,0,0.15);
    overflow: hidden;
  }
  .brand-square { position: absolute; background: var(--teal); }
  .brand-name {
    position: absolute;
    color: var(--teal);
    font-weight: 400;
    text-transform: uppercase;
    letter-spacing: 0.06em;
    white-space: nowrap;
  }
  .contact-block {
    position: absolute;
    display: flex;
    align-items: flex-start;
  }
  .contact-list { list-style: none; }
  .contact-list li { display: flex; align-items: center; white-space: nowrap; }
  .contact-list svg { flex: none; }
  .address { white-space: nowrap; }
  .practice-band {
    position: absolute; left: 0; right: 0; bottom: 0;
    background: var(--teal);
    color: var(--paper);
    display: flex; align-items: center;
    white-space: nowrap;
  }
  .tagline {
    position: absolute;
    color: var(--teal);
    text-transform: uppercase;
    white-space: nowrap;
  }

  /* Business card back */
  .card-back { left: 40px; top: 56px; width: 360px; height: 205px; background: var(--grey-dark); }
  .card-back .brand-name {
    left: 0; right: 0; top: 82px; text-align: center;
    color: var(--paper); font-size: 20px;
  }
  .card-back .tag-band {
    position: absolute; left: 0; right: 0; top: 163px; height: 18px;
    background: var(--grey-light);
    display: flex; align-items: center; justify-content: center;
    color: var(--teal); font-size: 8px; font-weight: 500; letter-spacing: 0.2em;
  }

  /* Business card front */
  .card-front { left: 40px; top: 290px; width: 360px; height: 205px; }
  .card-front .brand-square { left: 24px; top: 0; width: 56px; height: 46px; }
  .card-front .brand-name { left: 16px; top: 76px; font-size: 12px; }
  .card-front .person { position: absolute; left: 116px; top: 38px; }
  .card-front .person-name { color: var(--teal); font-size: 8px; font-weight: 600; }
  .card-front .person-role { font-size: 7px; }
  .card-front .contact-block { left: 116px; top: 64px; flex-direction: column; gap: 6px; font-size: 7px; line-height: 10px; }
  .card-front .contact-list li { gap: 4px; }
  .card-front .address { line-height: 9px; }
  .card-front .practice-band { height: 14px; padding-left: 10px; font-size: 7px; font-weight: 600; }

  /* Envelope */
  .envelope { left: 40px; top: 545px; width: 440px; height: 190px; }
  .envelope .brand-square { left: 20px; top: 0; width: 64px; height: 50px; }
  .envelope .brand-name { left: 14px; top: 76px; font-size: 12px; }
  .envelope .contact-block { left: 106px; top: 12px; gap: 18px; font-size: 8px; line-height: 11px; }
  .envelope .contact-list li { gap: 4px; }
  .envelope .tagline { right: 12px; bottom: 28px; font-size: 8px; letter-spacing: 0.18em; }
  .envelope .practice-band { height: 22px; padding-left: 14px; font-size: 8px; letter-spacing: 0.04em; }

  /* Letterhead */
  .letterhead { left: 500px; top: 56px; width: 656px; height: 1084px; }
  .letterhead .brand-square { left: 34px; top: 0; width: 78px; height: 62px; }
  .letterhead .brand-name { left: 30px; top: 108px; font-size: 15px; }
  .letterhead .contact-block { left: 146px; top: 24px; gap: 26px; font-size: 10px; line-height: 13px; }
  .letterhead .contact-list li { gap: 5px; }
  .letterhead .tagline { right: 14px; bottom: 36px; font-size: 10px; letter-spacing: 0.18em; }
  .letterhead .practice-band { height: 30px; padding-left: 18px; font-size: 10px; letter-spacing: 0.02em; }
</style>
</head>
<body>

<svg width="0" height="0" style="position:absolute" aria-hidden="true">
  <defs>
    <symbol id="icon-phone" viewBox="0 0 10 10">
      <rect width="10" height="10" rx="2" fill="#2ab5a3"/>
      <path d="M3 2.3 L4.2 3.6 L3.6 4.3 Q4.6 5.9 5.8 6.4 L6.5 5.8 L7.7 7 L7 7.8 Q4.2 7.6 2.3 3.1 Z" fill="#fff"/>
    </symbol>
    <symbol id="icon-mail" viewBox="0 0 10 10">
      <rect width="10" height="10" rx="2" fill="#2ab5a3"/>
      <rect x="2" y="3" width="6" height="4" fill="#fff"/>
      <path d="M2 3 L5 5.3 L8 3" fill="none" stroke="#2ab5a3" stroke-width="0.7"/>
    </symbol>
    <symbol id="icon-web" viewBox="0 0 10 10">
      <circle cx="5" cy="5" r="5" fill="#2ab5a3"/>
      <circle cx="5" cy="5" r="2.8" fill="none" stroke="#fff" stroke-width="0.7"/>
      <path d="M2.2 5 H7.8 M5 2.2 V7.8" stroke="#fff" stroke-width="0.6"/>
    </symbol>
  </defs>
</svg>

<section class="sheet card-back" aria-label="Business card back">
  <div class="brand-name">Varneck Law</div>
  <div class="tag-band">RELATIONSHIPS. RESPECT. RESULT</div>
</section>

<section class="sheet card-front" aria-label="Business card front">
  <div class="brand-square"></div>
  <div class="brand-name">Varneck Law</div>
  <div class="person">
    <div class="person-name">Mara Varneck</div>
    <div class="person-role">Trial Lawyer</div>
  </div>
  <div class="contact-block">
    <ul class="contact-list">
      <li><svg width="7" height="7"><use href="#icon-phone"/></svg>(555) 014-2790</li>
      <li><svg width="7" height="7"><use href="#icon-mail"/></svg>mara@varneck-law-example.com</li>
      <li><svg width="7" height="7"><use href="#icon-web"/></svg>www.varneck-law-example.com</li>
    </ul>
    <div class="address">Southern California,<br>1480 Harborline Ave. #300<br>Seaview Beach, CA 90000</div>
  </div>
  <div class="practice-band">Practice areas, Criminal Law, Civil Litigation/Personal Injury, Restraining</div>
</section>

<section class="sheet envelope" aria-label="Envelope">
  <div class="brand-square"></div>
  <div class="brand-name">Varneck Law</div>
  <div class="contact-block">
    <ul class="contact-list">
      <li><svg width="8" height="8"><use href="#icon-phone"/></svg>(555) 014-2790</li>
      <li><svg width="8" height="8"><use href="#icon-mail"/></svg>mara@varneck-law-example.com</li>
      <li><svg width="8" height="8"><use href="#icon-web"/></svg>www.varneck-law-example.com</li>
    </ul>
    <div class="address">Southern California,<br>1480 Harborline Ave. #300<br>Seaview Beach, CA 90000</div>
  </div>
  <div class="tagline">Relationships. Respect. Result</div>
  <div class="practice-band">Practice areas, Criminal Law, Civil Litigation/Personal Injury, Restraining</div>
</section>

<section class="sheet letterhead" aria-label="Letterhead">
  <div class="brand-square"></div>
  <div class="brand-name">Varneck Law</div>
  <div class="contact-block">
    <ul class="contact-list">
      <li><svg width="9" height="9"><use href="#icon-phone"/></svg>(555) 014-2790</li>
      <li><svg width="9" height="9"><use href="#icon-mail"/></svg>mara@varneck-law-example.com</li>
      <li><svg width="9" height="9"><use href="#icon-web"/></svg>www.varneck-law-example.com</li>
    </ul>
    <div class="address">Southern California,<br>1480 Harborline Ave. #300<br>Seaview Beach, CA 90000</div>
  </div>
  <div class="tagline">Relationships. Respect. Result</div>
  <div class="practice-band">Practice areas, Criminal Law, Civil Litigation/Personal Injury, Restraining</div>
</section>

</body>
</html>
```